Business Card for Quillmark Ledger - A cannabis publication for executives.

I'd like some business cards for Quillmark Ledger. The logo is done (great job!) and I need a card design I will use with PRINTLY. I made it a short project to allow time for printing before an event. These will be standard sized cards (final artwork size 3.66" x 2.16" at 300dpi) with a final card size of 3.5" x 2.0". (See PRINTLY.com if you need more info.) I might try rounded corners but am not sure yet. I think the design will work okay with rounded.

Quillmark Ledger will be a bi-weekly publication for the cannabis industry. It is targeted to investors and industry executives, not consumers or pot smokers. So our market is more B2B. However I am open to creativity and making the card something people remark on.

My contact for card:

Dana Merrow
Founder/CEO
dana@quillmarkledger.example

2740 Harlow Avenue
Boston MA 02135
(617)555-0194

Target Market(s)

Executives, Industry people and investors in the Cannabis sector.

Contact Information for Business Card

PRINTLY does do double sided and the second side can be the same or different images. Only one side is required but use of the second side would be a bonus.

Font styles to use
Serif
Sans Serif
Decorative

Colors

Designer to choose colors to be used in the design.

Requirements
Must have
• Logo, contact info
Nice to have
• Style and design to make the card stand out in a crowd.

```html
<!DOCTYPE html>
<html lang="en">
<head>
<meta charset="utf-8">
<title>Quillmark Ledger — Business Card</title>
<link rel="stylesheet" href="https://fonts.googleapis.com/css2?family=Open+Sans:wght@400;600;700&display=swap">
<style>
  :root {
    --brand-blue: #1273bd;
    --brand-green: #7bb03f;
    --card-white: #ffffff;
    --ink-dark: #333840;
    --backdrop: #2b2b2d;
  }
  html, body {
    margin: 0;
    padding: 0;
    width: 1200px;
    height: 880px;
    overflow: hidden;
    background: var(--backdrop);
    font-family: "Open Sans", Arial, sans-serif;
  }
  .canvas {
    position: relative;
    width: 1200px;
    height: 880px;
  }
  .card {
    position: absolute;
    left: 250px;
    width: 700px;
    height: 400px;
    border-radius: 26px;
    overflow: hidden;
  }
  .card-front {
    top: 30px;
    background: var(--brand-blue);
    display: flex;
    align-items: center;
    justify-content: center;
  }
  .card-back {
    top: 450px;
    background: var(--card-white);
  }
  .wordmark {
    display: flex;
    align-items: center;
    gap: 16px;
    font-weight: 600;
    letter-spacing: -0.5px;
    white-space: nowrap;
  }
  .wordmark-square {
    display: inline-block;
    flex: none;
  }
  .wordmark-front {
    color: var(--card-white);
    font-size: 52px;
  }
  .wordmark-front .wordmark-square {
    width: 48px;
    height: 48px;
    background: var(--card-white);
  }
  .wordmark-back {
    position: absolute;
    left: 38px;
    top: 128px;
    color: var(--brand-blue);
    font-size: 44px;
  }
  .wordmark-back .wordmark-square {
    width: 42px;
    height: 42px;
    background: var(--brand-green);
  }
  .wave-art {
    position: absolute;
    inset: 0;
    width: 700px;
    height: 400px;
  }
  .holder {
    position: absolute;
    right: 40px;
    top: 26px;
    text-align: left;
    line-height: 1.05;
  }
  .holder-name {
    color: var(--brand-blue);
    font-weight: 700;
    font-size: 22px;
  }
  .holder-title {
    color: var(--ink-dark);
    font-size: 17px;
  }
  .contact {
    position: absolute;
    right: 30px;
    top: 212px;
    text-align: right;
    color: var(--card-white);
    font-size: 15px;
    font-style: normal;
    line-height: 1.4;
    white-space: nowrap;
  }
  .contact-line {
    display: flex;
    justify-content: flex-end;
    align-items: center;
    gap: 8px;
  }
  .contact-icon {
    width: 15px;
    height: 15px;
    flex: none;
  }
</style>
</head>
<body>
<main class="canvas">

  <section class="card card-front" aria-label="Card front">
    <div class="wordmark wordmark-front">
      <span class="wordmark-square"></span>
      <span class="wordmark-name">Quillmark Ledger</span>
    </div>
  </section>

  <section class="card card-back" aria-label="Card back">
    <svg class="wave-art" viewBox="0 0 700 400" aria-hidden="true">
      <path d="M0,348 C160,330 300,292 352,190 C330,292 210,352 0,372 Z" fill="var(--brand-green)"/>
      <path d="M700,70 C545,72 450,150 388,250 C340,335 260,382 90,400 L700,400 Z" fill="var(--brand-blue)"/>
      <path d="M700,92 C560,95 470,165 410,262 C370,342 290,388 130,400" fill="none" stroke="var(--card-white)" stroke-width="7"/>
    </svg>

    <div class="wordmark wordmark-back">
      <span class="wordmark-square"></span>
      <span class="wordmark-name">Quillmark Ledger</span>
    </div>

    <div class="holder">
      <div class="holder-name">Dana Merrow</div>
      <div class="holder-title">Founder/CEO</div>
    </div>

    <address class="contact">
      <div class="contact-line">2740 Harlow Avenue</div>
      <div class="contact-line">Boston MA 02135</div>
      <div class="contact-line">(617)555-0194
        <svg class="contact-icon" viewBox="0 0 16 16" aria-hidden="true">
          <rect x="0.5" y="0.5" width="15" height="15" rx="2" fill="var(--card-white)"/>
          <path d="M4.5 3.5 l2 0 l1 3 l-1.3 1 a7 7 0 0 0 2.3 2.3 l1-1.3 l3 1 l0 2 a1.5 1.5 0 0 1 -1.5 1.5 A8 8 0 0 1 3 5 a1.5 1.5 0 0 1 1.5 -1.5 Z" fill="var(--brand-blue)"/>
        </svg>
      </div>
      <div class="contact-line">dana@quillmarkledger.example
        <svg class="contact-icon" viewBox="0 0 16 16" aria-hidden="true">
          <rect x="0.5" y="0.5" width="15" height="15" rx="2" fill="var(--card-white)"/>
          <rect x="3" y="4.5" width="10" height="7" fill="none" stroke="var(--brand-blue)" stroke-width="1.4"/>
          <path d="M3 4.5 L8 8.5 L13 4.5" fill="none" stroke="var(--brand-blue)" stroke-width="1.4"/>
        </svg>
      </div>
    </address>
  </section>

</main>
</body>
</html>
```